BrightKeel Business Card Contest

We are looking for a modern business card that catches attention and is unique. Attached is the brand guide and logo files. Please note that the back side (not the side with our name and info) with be UV raise printed, so have fun with the design there. We want to include Name, Title, Phone number, email, website.

Contact Information for Business Card

Please see project description

```html
<!DOCTYPE html>
<html lang="en">
<head>
<meta charset="utf-8">
<title>BrightKeel Business Card</title>
<link rel="stylesheet" href="https://fonts.googleapis.com/css2?family=Questrial&display=swap">
<style>
  :root {
    --bg: #2b2b2d;
    --card: #ffffff;
    --card-shade: #ececec;
    --ink: #1d1d1f;
    --muted: #555a60;
    --red: #d3261f;
    --orange: #e0791c;
    --slate: #a3acba;
    --sky: #22b4dc;
    --blue: #1f6fb6;
    --navy: #1b3474;
  }
  * { box-sizing: border-box; margin: 0; padding: 0; }
  html, body { width: 1200px; height: 900px; overflow: hidden; }
  body {
    background: var(--bg);
    font-family: "Questrial", "Century Gothic", sans-serif;
    position: relative;
  }
  .card {
    position: absolute;
    width: 560px;
    height: 320px;
    background: linear-gradient(100deg, var(--card-shade) 0%, var(--card) 70%);
    overflow: hidden;
    box-shadow: 0 14px 30px rgba(0,0,0,.45);
  }
  .card--back { left: 80px; top: 90px; }
  .card--front { left: 560px; top: 490px; }

  .accent-band {
    position: absolute;
    top: 0;
    bottom: 0;
    width: 150px;
    background: linear-gradient(180deg,
      var(--red) 0 8%, var(--orange) 8% 16%, var(--slate) 16% 40%,
      var(--sky) 40% 58%, var(--blue) 58% 80%, var(--navy) 80% 100%);
  }
  .card--back .accent-band { right: 0; }
  .card--front .accent-band { left: 0; }

  .back-url {
    position: absolute;
    left: 46px;
    top: 145px;
    font-size: 26px;
    letter-spacing: 7px;
    color: var(--ink);
  }

  .front-info {
    position: absolute;
    left: 210px;
    right: 30px;
    top: 40px;
    text-align: center;
  }
  .brand {
    display: inline-flex;
    align-items: center;
    gap: 10px;
    font-size: 40px;
    color: var(--ink);
  }
  .brand-square {
    width: 22px;
    height: 22px;
    background: var(--blue);
  }
  .person-name {
    margin-top: 26px;
    font-size: 18px;
    letter-spacing: .5px;
    color: var(--red);
  }
  .person-title {
    font-size: 14px;
    color: var(--muted);
  }
  .contact-list {
    list-style: none;
    display: inline-block;
    margin-top: 26px;
    text-align: left;
    font-size: 14px;
    color: var(--muted);
  }
  .contact-list li {
    display: flex;
    align-items: center;
    gap: 8px;
    line-height: 26px;
  }
  .contact-list svg { width: 14px; height: 14px; fill: var(--sky); flex: none; }
</style>
</head>
<body>
  <section class="card card--back" aria-label="Card back">
    <p class="back-url">www.BrightKeel.com</p>
    <div class="accent-band"></div>
  </section>

  <section class="card card--front" aria-label="Card front">
    <div class="accent-band"></div>
    <div class="front-info">
      <div class="brand"><span class="brand-square"></span>BrightKeel</div>
      <p class="person-name">MARA ELLISON</p>
      <p class="person-title">Director</p>
      <ul class="contact-list">
        <li>
          <svg viewBox="0 0 16 16" aria-hidden="true"><path d="M3.6 1.2l2.3 2.6-1.3 1.9c.9 1.9 2.4 3.4 4.3 4.3l1.9-1.3 2.6 2.3-1.5 2.1C6.7 13.4 2.6 9.3 1.5 2.7z"/></svg>
          555-210-4800
        </li>
        <li>
          <svg viewBox="0 0 16 16" aria-hidden="true"><path d="M1 3h14v10H1zM2.5 4.5L8 9l5.5-4.5v-.2H2.5z" fill-rule="evenodd"/></svg>
          info@BrightKeel.com
        </li>
        <li>
          <svg viewBox="0 0 16 16" aria-hidden="true"><circle cx="8" cy="8" r="6.5" fill="none" stroke="#22b4dc" stroke-width="1.4"/><path d="M1.5 8h13M8 1.5c-3 3.5-3 9.5 0 13M8 1.5c3 3.5 3 9.5 0 13" fill="none" stroke="#22b4dc" stroke-width="1.2"/></svg>
          www.BrightKeel.com
        </li>
      </ul>
    </div>
  </section>
</body>
</html>
```